Re-Design the flow of the Orvane Framework

The orvane framework is a 10 step model that helps teams/organizations become high performing. Attached the model which i created. I love the design as it is but i used a template i don't owe the rights of so i would like to use this platform to see what you can come up with the redesign this flow while keeping the key elements in place. I like the flow, i like the cleanness and i like it to be compact.

Target Market(s)

Organizational change / Leadership/ Consultancy

Industry/Entity Type

Leadership

Requirements
Must have
• Keep as much as possible the flow and feel of the attached
Nice to have
• -Maybe some twist in how the different parts connect (not a must)
Should not have
• Less or more steps than added in the attached file

```html
<!DOCTYPE html>
<html lang="en">
<head>
<meta charset="utf-8">
<title>The Orvane Framework</title>
<link rel="stylesheet" href="https://fonts.googleapis.com/css2?family=Montserrat:wght@500;600;700;800&display=swap">
<style>
  :root {
    --page: #dcdcdc;
    --card: #ffffff;
    --panel: #b9b9b9;
    --track: #ebebeb;
    --ink: #333333;
    --ink-soft: #454545;
    --brand-purple: #5e3f9a;
    --band-blue: #0a6aad;
    --chevron: #8a8a8a;
    --green: #9bc63a;
    --teal: #35aeb4;
    --sky: #1f8fcc;
    --navy: #0c5fa6;
    --navy-deep: #0a5494;
    --violet: #5c3f97;
    --magenta: #9c3596;
    --crimson: #d42d5f;
    --orange: #f26a22;
    --amber: #dea412;
  }
  html, body {
    margin: 0;
    width: 1029px;
    height: 1200px;
    overflow: hidden;
    background: var(--page);
  }
  .framework-card {
    position: absolute;
    top: 236px;
    left: 0;
    width: 1029px;
    height: 727px;
    background: var(--card);
  }
  .framework-card svg { display: block; font-family: "Montserrat", sans-serif; }
  .title { font-size: 62px; font-weight: 800; }
  .title-accent { fill: var(--brand-purple); }
  .title-main { fill: var(--ink); }
  .tagline { font-size: 16.5px; font-weight: 700; fill: #fff; letter-spacing: 0.3px; }
  .track { fill: none; stroke: var(--track); stroke-width: 16; }
  .chevron { fill: var(--chevron); }
  .node-ring { stroke: #fff; stroke-width: 4; }
  .step-number-disc { fill: var(--ink); stroke: #fff; stroke-width: 2; }
  .step-number { font-size: 11px; font-weight: 700; fill: #fff; }
  .step-label { font-size: 12px; font-weight: 700; fill: var(--ink); }
  .phase-label { font-size: 17px; font-weight: 700; fill: var(--ink-soft); }
  .phase-label--light { fill: #fff; }
  .phase-divider { stroke: #fff; stroke-width: 2; }
  .group-label { font-size: 16px; font-weight: 700; fill: #fff; letter-spacing: 1.5px; }
  .group-label--lower { letter-spacing: 0.5px; font-size: 17px; }
  .group-line { stroke: #fff; stroke-width: 3; }
  .restart-label { font-size: 12px; font-weight: 700; fill: #fff; letter-spacing: 0.4px; }
  .goal-title { font-size: 14px; font-weight: 700; fill: var(--ink-soft); }
  .goal-list { font-size: 10px; font-weight: 500; fill: #555; }
</style>
</head>
<body>
<div class="framework-card">
<svg width="1029" height="727" viewBox="0 0 1029 727" aria-labelledby="fw-title">
  <defs>
    <symbol id="icon-heart" viewBox="-20 -20 40 40">
      <path d="M0,15 C-14,5 -19,-3 -15,-10 C-11,-16 -3,-14 0,-8 C3,-14 11,-16 15,-10 C19,-3 14,5 0,15Z" fill="#fff"/>
      <polyline points="-12,0 -5,0 -2,-6 2,6 5,-2 12,-2" fill="none" stroke="currentColor" stroke-width="2"/>
    </symbol>
    <symbol id="icon-team" viewBox="-20 -20 40 40">
      <g fill="#fff">
        <circle cx="-11" cy="-11" r="3.5"/><rect x="-15" y="-6" width="8" height="20" rx="2"/>
        <circle cx="0" cy="-11" r="3.5"/><rect x="-4" y="-6" width="8" height="20" rx="2"/>
        <circle cx="11" cy="-11" r="3.5"/><rect x="7" y="-6" width="8" height="20" rx="2"/>
      </g>
    </symbol>
    <symbol id="icon-target" viewBox="-20 -20 40 40">
      <g fill="none" stroke="#fff" stroke-width="2.5">
        <circle r="12"/><circle r="6"/>
        <line x1="0" y1="-18" x2="0" y2="-8"/><line x1="0" y1="8" x2="0" y2="18"/>
        <line x1="-18" y1="0" x2="-8" y2="0"/><line x1="8" y1="0" x2="18" y2="0"/>
      </g>
      <circle r="2.5" fill="#fff"/>
    </symbol>
    <symbol id="icon-scope" viewBox="-20 -20 40 40">
      <g stroke="#fff" stroke-width="3" stroke-linecap="round" fill="none">
        <line x1="-14" y1="-4" x2="12" y2="-14"/>
        <line x1="0" y1="-8" x2="-7" y2="14"/><line x1="0" y1="-8" x2="7" y2="14"/>
      </g>
    </symbol>
    <symbol id="icon-growth" viewBox="-20 -20 40 40">
      <g fill="#fff">
        <circle cx="-11" cy="-11" r="3"/><rect x="-14" y="-7" width="6" height="12" rx="2"/>
        <circle cx="-1" cy="-11" r="3"/><rect x="-4" y="-7" width="6" height="12" rx="2"/>
        <circle cx="9" cy="-11" r="3"/><rect x="6" y="-7" width="6" height="12" rx="2"/>
      </g>
      <polyline points="-16,14 -6,6 0,10 14,-2" fill="none" stroke="#fff" stroke-width="2.5"/>
      <polygon points="16,-5 9,-3 14,3" fill="#fff"/>
    </symbol>
    <symbol id="icon-gear" viewBox="-20 -20 40 40">
      <circle r="13" fill="#fff"/>
      <circle r="6" fill="none" stroke="currentColor" stroke-width="3"/>
      <g stroke="currentColor" stroke-width="3">
        <line x1="0" y1="-11" x2="0" y2="-7"/><line x1="0" y1="7" x2="0" y2="11"/>
        <line x1="-11" y1="0" x2="-7" y2="0"/><line x1="7" y1="0" x2="11" y2="0"/>
      </g>
    </symbol>
    <symbol id="icon-star" viewBox="-20 -20 40 40">
      <polygon points="0,-17 4.5,-6 16,-5.5 7,2 10,14 0,7.5 -10,14 -7,2 -16,-5.5 -4.5,-6" fill="#fff"/>
    </symbol>
    <symbol id="icon-trophy" viewBox="-20 -20 40 40">
      <path d="M-9,-15 H9 V-4 A9,9 0 0 1 -9,-4 Z" fill="#fff"/>
      <path d="M-9,-12 H-15 V-7 A6,6 0 0 0 -8,-1 M9,-12 H15 V-7 A6,6 0 0 1 8,-1" fill="none" stroke="#fff" stroke-width="2.5"/>
      <rect x="-2" y="4" width="4" height="7" fill="#fff"/>
      <rect x="-8" y="11" width="16" height="4" rx="1" fill="#fff"/>
    </symbol>
    <symbol id="icon-monitor" viewBox="-20 -20 40 40">
      <circle cx="-2" cy="-4" r="11" fill="none" stroke="#fff" stroke-width="3"/>
      <polyline points="-9,-3 -5,-3 -3,-8 0,2 2,-4 5,-4" fill="none" stroke="#fff" stroke-width="2"/>
      <line x1="5" y1="7" x2="11" y2="17" stroke="#fff" stroke-width="4" stroke-linecap="round"/>
    </symbol>
    <polygon id="chev-right" points="-4,-6 4,0 -4,6"/>
  </defs>

  <title id="fw-title">The Orvane Framework</title>

  <!-- Heading -->
  <text class="title" x="514" y="88" text-anchor="middle"><tspan class="title-accent">THE ORVANE </tspan><tspan class="title-main">FRAMEWORK</tspan></text>
  <rect x="22" y="100" width="985" height="37" fill="var(--band-blue)"/>
  <text class="tagline" x="514" y="124.5" text-anchor="middle">LIBERATE THE WORKPLACE UNLEASHING VALUE THROUG PURPOSE AT EVERY LEVEL OF SCALE</text>

  <!-- Panel -->
  <rect x="22" y="150" width="985" height="562" fill="var(--panel)"/>

  <!-- Continuous track: foundation on top, excellence below, closing back to the start -->
  <path class="track" d="M175,330 H855 A115,115 0 0 1 855,560 H175 A115,115 0 0 1 175,330 Z"/>

  <!-- Direction chevrons -->
  <g class="chevron">
    <use href="#chev-right" transform="translate(267,330)"/>
    <use href="#chev-right" transform="translate(391,330)"/>
    <use href="#chev-right" transform="translate(515,330)"/>
    <use href="#chev-right" transform="translate(639,330)"/>
    <use href="#chev-right" transform="translate(763,330)"/>
    <use href="#chev-right" transform="translate(970,445) rotate(90)"/>
    <use href="#chev-right" transform="translate(763,560) rotate(180)"/>
    <use href="#chev-right" transform="translate(639,560) rotate(180)"/>
    <use href="#chev-right" transform="translate(515,560) rotate(180)"/>
    <use href="#chev-right" transform="translate(365,560) rotate(180)"/>
    <use href="#chev-right" transform="translate(60,445) rotate(-90)"/>
  </g>

  <!-- Group labels -->
  <g class="groups">
    <text class="group-label" x="329" y="206" text-anchor="middle">SELF DIRECTION</text>
    <line class="group-line" x1="170" y1="200" x2="228" y2="200"/>
    <line class="group-line" x1="430" y1="200" x2="480" y2="200"/>
    <polygon points="490,200 478,193 478,207" fill="#fff"/>

    <text class="group-label" x="701" y="206" text-anchor="middle">HUMAN EXPERIENCE</text>
    <line class="group-line" x1="545" y1="200" x2="594" y2="200"/>
    <line class="group-line" x1="808" y1="200" x2="852" y2="200"/>
    <polygon points="862,200 850,193 850,207" fill="#fff"/>

    <text class="group-label group-label--lower" x="639" y="694" text-anchor="middle">unlash engagement</text>
    <polygon points="430,688 442,681 442,695" fill="#fff"/>
    <line class="group-line" x1="440" y1="688" x2="540" y2="688"/>
    <line class="group-line" x1="738" y1="688" x2="840" y2="688"/>
  </g>

  <!-- Phase captions inside the track -->
  <text class="phase-label" x="515" y="405" text-anchor="middle">Capabilities driving a solid foundation</text>
  <line class="phase-divider" x1="300" y1="445" x2="800" y2="445"/>
  <text class="phase-label phase-label--light" x="515" y="497" text-anchor="middle">Capabilities maximizing excellence</text>

  <!-- Restart marker on the closing arc -->
  <text class="restart-label" x="88" y="425">(RE)START HERE</text>
  <text class="restart-label" x="88" y="475">(RE)INVENT HERE</text>
  <line x1="100" y1="450" x2="200" y2="450" stroke="#fff" stroke-width="3"/>
  <polygon points="88,450 100,443 100,457" fill="#fff"/>

  <!-- Steps 1–6 -->
  <g class="step">
    <circle class="node-ring" cx="205" cy="330" r="30" fill="var(--green)"/>
    <use href="#icon-heart" x="187" y="312" width="36" height="36" color="var(--green)"/>
    <circle class="step-number-disc" cx="227" cy="352" r="10"/><text class="step-number" x="227" y="356" text-anchor="middle">1</text>
    <text class="step-label" text-anchor="middle"><tspan x="205" y="244">Identify</tspan><tspan x="205" dy="14">Purpose</tspan><tspan x="205" dy="14">Activators</tspan><tspan x="205" dy="14">(Vision)</tspan></text>
  </g>
  <g class="step">
    <circle class="node-ring" cx="329" cy="330" r="30" fill="var(--teal)"/>
    <use href="#icon-scope" x="311" y="312" width="36" height="36"/>
    <circle class="step-number-disc" cx="351" cy="352" r="10"/><text class="step-number" x="351" y="356" text-anchor="middle">2</text>
    <text class="step-label" text-anchor="middle"><tspan x="329" y="244">Identify</tspan><tspan x="329" dy="14">Purpose</tspan><tspan x="329" dy="14">Activators</tspan><tspan x="329" dy="14">(Vision)</tspan></text>
  </g>
  <g class="step">
    <circle class="node-ring" cx="453" cy="330" r="30" fill="var(--sky)"/>
    <use href="#icon-target" x="435" y="312" width="36" height="36"/>
    <circle class="step-number-disc" cx="475" cy="352" r="10"/><text class="step-number" x="475" y="356" text-anchor="middle">3</text>
    <text class="step-label" text-anchor="middle"><tspan x="453" y="258">Develop a</tspan><tspan x="453" dy="14">Master plan</tspan><tspan x="453" dy="14">(strategy)</tspan></text>
  </g>
  <g class="step">
    <circle class="node-ring" cx="577" cy="330" r="30" fill="var(--navy)"/>
    <use href="#icon-team" x="559" y="312" width="36" height="36"/>
    <circle class="step-number-disc" cx="599" cy="352" r="10"/><text class="step-number" x="599" y="356" text-anchor="middle">4</text>
    <text class="step-label" text-anchor="middle"><tspan x="577" y="244">Cultivate</tspan><tspan x="577" dy="14">Psychological</tspan><tspan x="577" dy="14">Safety and</tspan><tspan x="577" dy="14">Ownership</tspan></text>
  </g>
  <g class="step">
    <circle class="node-ring" cx="701" cy="330" r="30" fill="var(--navy-deep)"/>
    <use href="#icon-heart" x="683" y="312" width="36" height="36" color="var(--navy-deep)"/>
    <circle class="step-number-disc" cx="723" cy="352" r="10"/><text class="step-number" x="723" y="356" text-anchor="middle">5</text>
    <text class="step-label" text-anchor="middle"><tspan x="701" y="244">Unlock culture</tspan><tspan x="701" dy="14">of personal</tspan><tspan x="701" dy="14">growth &amp;</tspan><tspan x="701" dy="14">development</tspan></text>
  </g>
  <g class="step">
    <circle class="node-ring" cx="825" cy="330" r="30" fill="var(--violet)"/>
    <use href="#icon-growth" x="807" y="312" width="36" height="36"/>
    <circle class="step-number-disc" cx="847" cy="352" r="10"/><text class="step-number" x="847" y="356" text-anchor="middle">6</text>
    <text class="step-label" text-anchor="middle"><tspan x="825" y="244">Unlock</tspan><tspan x="825" dy="14">culture of</tspan><tspan x="825" dy="14">personal growth</tspan><tspan x="825" dy="14">&amp; development</tspan></text>
  </g>

  <!-- Steps 7–10 -->
  <g class="step">
    <circle class="node-ring" cx="825" cy="560" r="30" fill="var(--magenta)"/>
    <use href="#icon-gear" x="807" y="542" width="36" height="36" color="var(--magenta)"/>
    <circle class="step-number-disc" cx="847" cy="582" r="10"/><text class="step-number" x="847" y="586" text-anchor="middle">7</text>
    <text class="step-label" text-anchor="middle"><tspan x="825" y="612">Prioritize</tspan><tspan x="825" dy="14">Feedback &amp;</tspan><tspan x="825" dy="14">Transparency</tspan></text>
  </g>
  <g class="step">
    <circle class="node-ring" cx="701" cy="560" r="30" fill="var(--crimson)"/>
    <use href="#icon-star" x="683" y="542" width="36" height="36"/>
    <circle class="step-number-disc" cx="723" cy="582" r="10"/><text class="step-number" x="723" y="586" text-anchor="middle">8</text>
    <text class="step-label" text-anchor="middle"><tspan x="701" y="612">Empower the</tspan><tspan x="701" dy="14">community from</tspan><tspan x="701" dy="14">bottom-up</tspan></text>
  </g>
  <g class="step">
    <circle class="node-ring" cx="577" cy="560" r="30" fill="var(--orange)"/>
    <use href="#icon-trophy" x="559" y="542" width="36" height="36"/>
    <circle class="step-number-disc" cx="599" cy="582" r="10"/><text class="step-number" x="599" y="586" text-anchor="middle">9</text>
    <text class="step-label" text-anchor="middle"><tspan x="577" y="612">Put excellent</tspan><tspan x="577" dy="14">(team) performance</tspan><tspan x="577" dy="14">in the spotlight</tspan></text>
  </g>
  <g class="step">
    <circle class="node-ring" cx="453" cy="560" r="30" fill="var(--amber)"/>
    <use href="#icon-monitor" x="435" y="542" width="36" height="36"/>
    <circle class="step-number-disc" cx="475" cy="582" r="10"/><text class="step-number" x="475" y="586" text-anchor="middle">10</text>
    <text class="step-label" text-anchor="middle"><tspan x="453" y="612">Monitor</tspan><tspan x="453" dy="14">engagement</tspan><tspan x="453" dy="14">Real-time</tspan></text>
  </g>

  <!-- Goal -->
  <g class="goal">
    <circle cx="265" cy="560" r="40" fill="var(--brand-purple)" stroke="#fff" stroke-width="4"/>
    <g fill="none" stroke="#fff" stroke-width="2.5" stroke-linejoin="round">
      <polygon points="251,548 279,548 288,558 265,582 242,558"/>
      <polyline points="242,558 288,558"/>
      <polyline points="256,558 265,582 274,558"/>
      <polyline points="251,548 256,558 265,548 274,558 279,548"/>
    </g>
    <text class="goal-title" x="100" y="624">Reaching full potential of</text>
    <text class="goal-title" x="100" y="641">people and organization</text>
    <text class="goal-list" x="100" y="659">• Productivity up to 800%</text>
    <text class="goal-list" x="100" y="671">• Employee engagement &gt;90%</text>
    <text class="goal-list" x="100" y="683">• Max discretionary effort gap</text>
    <text class="goal-list" x="100" y="695">• High resilience to change</text>
  </g>
</svg>
</div>
</body>
</html>
```